Heath Weight Loss Retreat Website

The brief:
FitWave is a provider of health & weight loss retreats and wish to redesign their main website. The website needs to provide detailed information about the company’s services whilst gathering the maximum number of leads possible. The website does not aim to get clients to ‘book now’ but to request further information, or ask a question generating a lead/opportunity for the business.

Primary objectives of website
• Gather leads for products (not necessarily to book at that point, but to ‘request more info’)
• Provide detailed information about the health and fitness programs on offer

Demographic Considerations
• Target age group: 30-50
• Predominant client base are female but website should be gender neutral due to some men attending

Design considerations
• Essentially selling ‘travel experiences’ and ‘life transformations’ so needs to be lots of images to display (similar to a hotel website for example)
• Images need to display real people – i.e. larger people, rather than super thin
• Not too much use of flash
• SEO friendly (we have good rankings at present)
• Will be implemented into Joomla, so please consider this on the design
• Colours should be ‘warm’ and ‘friendly’ and gender neutral

Project Requirements & Expectations
Please supply your design ideas with:
• At least 1 (preferably more) homepage examples
• At least 1 (preferably more) internal page examples
Once a preferred design has been selected the following will be produced, tweaked and approved:
• Homepage + 1 internal landing page + 1 internal main page + 1 contact page + 1 info request page

Attachments
We have attached both a homepage and internal page example which demonstates the type of content needed and the calls to action. This is for demonstration purposes only so please ignore colours, fonts, etc and provide your best designs based on a general layout as per attached.

Images:
A selection of example images has been attached. For the homepage images of the retreats themselves should be used alongside images of ‘larger people’.

Further information:
Please contact Martin Colbeck at martin.colbeck@pemberlyfiles.com.au

Target Market(s)

Overweight females aged 30-50 are the main target market. However must be gender neutral due to some men using product.

Industry/Entity Type

Weight

Requirements
Should not have
• Not too much flash

```html
<!DOCTYPE html>
<html lang="en">
<head>
<meta charset="utf-8">
<title>FitWave Weight Loss Retreat</title>
<link rel="stylesheet" href="https://fonts.googleapis.com/css2?family=Arimo:ital,wght@0,400;0,700;1,400;1,700&display=swap">
<style>
:root{
  --blue:#2b6ea8;
  --blue-dark:#1f5687;
  --blue-foot:#2d6a9c;
  --orange:#f08a1c;
  --green:#74b330;
  --green-dark:#4f8a1a;
  --lime:#c9e27f;
  --red:#d9201f;
  --pale:#dae8f3;
  --ink:#222;
  --line:#cfcfcf;
  --white:#fff;
}
*{box-sizing:border-box;margin:0;padding:0}
html,body{width:1200px;height:2182px;overflow:hidden;background:var(--white)}
body{position:relative;font-family:"Arimo",Arial,sans-serif;color:var(--ink);font-size:15px}
a{color:inherit;text-decoration:none}
.abs{position:absolute}

/* header */
.brand{left:28px;top:24px;font-size:52px;font-weight:700;color:var(--orange);line-height:1}
.brand-sub{left:30px;top:80px;font-size:15px;font-weight:700;color:var(--green-dark);letter-spacing:.5px}
.mag-offer{left:907px;top:9px;width:265px;height:94px;border:1px solid var(--line);display:flex;align-items:center;gap:14px;padding:10px}
.mag-cover{width:92px;height:70px;flex:none;background:linear-gradient(160deg,#eee,#c8c8c8)}
.mag-text{font-size:15px;font-weight:700;color:var(--green-dark);line-height:1.2;white-space:nowrap}
.mag-text span{display:block;font-weight:400;font-size:13px;color:var(--ink);margin-top:12px;text-align:right}

/* nav */
.main-nav{left:28px;top:122px;width:1144px;height:56px;background:linear-gradient(var(--blue),var(--blue-dark));display:flex;align-items:center;gap:56px;padding-left:24px}
.main-nav a{color:var(--white);font-weight:700;font-size:17px}

/* hero */
.hero{left:28px;top:188px;width:1144px;height:346px;background:linear-gradient(100deg,#5e6b3e 0%,#8a8a56 35%,#a7a88a 60%,#8f9a6f 100%)}
.hero-panel{left:614px;top:211px;width:534px;height:248px;background:rgba(255,255,255,.78);padding:20px 22px}
.hero-panel h1{font-size:23px;color:var(--blue-dark);white-space:nowrap}
.hero-panel h2{font-size:19px;color:var(--blue);font-weight:400;font-style:italic;margin:4px 0 14px}
.hero-panel p{font-size:15px;line-height:1.5;color:#333}
.btn-orange{left:910px;top:393px;width:212px;height:44px;background:var(--orange);color:var(--white);font-size:20px;display:flex;align-items:center;justify-content:center;border-radius:3px}

/* left column */
.intro{left:28px;top:567px;width:469px;height:1257px;background:var(--pale);border-radius:6px;padding:20px 18px}
.intro .lead{font-size:17px;color:var(--blue-dark)}
.intro .quote{font-size:19px;font-weight:700;color:var(--blue-dark);margin:4px 0 16px;white-space:nowrap}
.btn-red{display:block;margin:0 auto;width:330px;height:42px;background:var(--red);color:var(--white);font-weight:700;font-size:16px;text-align:center;line-height:42px;border-radius:6px}
.more{text-align:right;margin:8px 66px 6px 0;font-size:13px;text-decoration:underline}
.perks{display:grid;grid-template-columns:1fr 1fr;gap:6px 0;margin:10px 0 14px;list-style:none}
.perks li{font-weight:700;font-size:15px;color:#333;display:flex;align-items:center;gap:8px}
.tick{width:15px;height:13px;flex:none}
.intro p.body{font-size:15px;letter-spacing:.6px;line-height:22.5px;color:#333;margin-bottom:14px}

/* programs */
.programs{left:520px;top:567px;width:324px}
.tab{height:40px;background:linear-gradient(90deg,var(--green-dark),var(--green));color:var(--white);font-size:21px;font-style:italic;padding:8px 10px;border-radius:2px 12px 0 0}
.book{font-size:14px;margin:8px 0 14px}
.book b{color:var(--orange)}
.prog{border-top:1px solid var(--line);padding:16px 0 12px}
.prog h3{font-size:17px;color:var(--blue-dark)}
.prog em{display:block;font-size:15px;color:var(--blue-dark);margin:3px 0 14px}
.prog .links{font-size:12.5px;text-decoration:underline;line-height:1.9;color:#333}

/* locations */
.locations{left:881px;top:567px;width:291px}
.grey-tab{height:40px;background:linear-gradient(90deg,#bbb,#e6e6e6);font-size:21px;font-style:italic;color:#444;padding:8px 12px;border-radius:2px 12px 0 0}
.loc-note{text-align:right;font-size:13px;margin:6px 0 14px}
.loc{position:relative;height:218px;margin-bottom:16px}
.loc .shot{position:absolute;inset:0}
.loc .cap{position:absolute;left:0;right:0;bottom:0;background:rgba(0,0,0,.55);color:var(--white);padding:8px 10px}
.cap h4{font-size:19px}
.cap p{font-size:12.5px;line-height:1.3}
.cap .l{font-size:12px;text-decoration:underline;margin-top:4px;display:flex;gap:12px}
.selector{border:1px solid var(--line);border-radius:6px;padding:10px 14px;height:116px}
.selector h5{font-size:16px;font-weight:400;color:#333}
.selector p{font-size:12px;color:#666;line-height:1.3}
.sel-row{display:flex;gap:10px;margin-top:10px}
.sel-row span{flex:1;height:28px;border:1px solid var(--line)}
.sel-row b{width:70px;height:28px;background:var(--orange);color:var(--white);font-size:14px;display:flex;align-items:center;justify-content:center;border-radius:3px}
.testi{margin-top:14px;border:1px solid var(--line);border-radius:6px;height:100px;padding:14px 18px;font-size:21px;font-style:italic;color:#444;text-align:center;background:linear-gradient(#fff,#f1f1f1)}
.testi-by{text-align:right;font-size:13px;margin-top:8px}

/* results */
.results{left:520px;top:1397px;width:652px;height:427px;border:1px solid var(--line);border-radius:6px;overflow:hidden}
.people{left:0;top:0;width:370px;height:166px;background:linear-gradient(90deg,#c9a17f,#a6704f 45%,#d8b49a)}
.real{left:376px;top:12px;width:270px}
.real h3{font-size:19px;color:var(--blue-dark);white-space:nowrap}
.real ul{list-style:none;font-size:13.5px;color:var(--blue-dark);line-height:1.6;margin-top:6px}
.real li::before{content:"";display:inline-block;width:8px;height:8px;border-radius:50%;background:var(--orange);margin-right:8px}
.real .rev{text-align:right;font-size:14px;font-weight:700;color:var(--blue-dark);margin-top:10px}
.achieved{left:0;top:166px;width:650px;height:259px;background:var(--lime);padding:10px 18px}
.achieved h4{font-size:21px;font-weight:400;color:var(--green-dark);margin-bottom:8px}
.ach-cols{display:grid;grid-template-columns:1fr 1fr;gap:0 20px}
.ach-cols ul{list-style:none}
.ach-cols li{font-size:15px;color:var(--blue-dark);display:flex;align-items:center;gap:10px;line-height:1.73}

/* footer */
.site-foot{left:0;top:1875px;width:1200px;height:307px;background:var(--blue-foot);color:var(--white)}
.foot-cols{left:28px;top:38px;display:flex}
.foot-col{width:208px;font-size:13px;line-height:1.62}
.foot-col h6{font-size:15px;margin-bottom:16px}
.foot-bar{left:0;top:249px;width:1200px;height:58px;background:#1d4d78;display:flex;align-items:center;justify-content:space-between;padding:0 28px;font-size:11.5px}
</style>
</head>
<body>

<header>
  <div class="abs brand">FitWave</div>
  <div class="abs brand-sub">WEIGHT LOSS RETREAT</div>
  <a class="abs mag-offer" href="#"><span class="mag-cover" role="img" aria-label="FitWave magazine cover"></span><span class="mag-text">FREE<br>FitWave Magazine<span>Request Now ▸</span></span></a>
</header>

<nav class="abs main-nav"><a href="#">THE BEST PROGRAMS</a><a href="#">THE BEST LOCATIONS</a><a href="#">ACT NOW AND GET RESULTS</a></nav>

<section>
  <div class="abs hero" role="img" aria-label="Smiling woman outdoors among greenery"></div>
  <div class="abs hero-panel">
    <h1>Amazing Weight Loss &amp; Fitness Results</h1>
    <h2>Lasting results &amp; 1st class facilities</h2>
    <p>FitWave has helped hundreds of people transform their lives,<br>lose weight, get fit and achieve lasting success. Let us help<br>you too...</p>
  </div>
  <a class="abs btn-orange" href="#">Request More Info</a>
</section>

<svg width="0" height="0" style="position:absolute"><defs><symbol id="tick" viewBox="0 0 15 13"><path d="M1 7l4 4L14 1" fill="none" stroke="#5aa21e" stroke-width="3"/></symbol></defs></svg>

<main>
  <section class="abs intro">
    <p class="lead">The FitWave program works - as one client put it.</p>
    <p class="quote">"The best weight loss experience of my life"</p>
    <a class="btn-red" href="#">Request a free information package</a>
    <p class="more">More Testimonials</p>
    <ul class="perks">
      <li><svg class="tick"><use href="#tick"/></svg>Stunning Locations</li>
      <li><svg class="tick"><use href="#tick"/></svg>For all shapes &amp; Sizes</li>
      <li><svg class="tick"><use href="#tick"/></svg>1st class facilities</li>
      <li><svg class="tick"><use href="#tick"/></svg>Delicious healthy food</li>
      <li><svg class="tick"><use href="#tick"/></svg>Amazing Results</li>
      <li><svg class="tick"><use href="#tick"/></svg>Expert support</li>
    </ul>
    <p class="body">Lorem ipsum dolor sit amet, consectetur adipisicing elit, sed do eiusmod tempor incididunt ut labore et dolore magna aliqua. Ut enim ad minim veniam, quis nostrud exercitation ullamco laboris nisi ut aliquip ex ea commodo consequat. Duis aute irure dolor in reprehenderit in voluptate velit esse cillum dolore eu fugiat nulla pariatur. Excepteur sint occaecat cupidatat non proident, sunt in culpa qui officia deserunt mollit anim id est laborum.</p>
    <p class="body">Lorem ipsum dolor sit amet, consectetur adipisicing elit, sed do eiusmod tempor incididunt ut labore et dolore magna aliqua. Ut enim ad minim veniam, quis nostrud exercitation ullamco laboris nisi ut aliquip ex ea commodo consequat. Duis aute irure dolor in reprehenderit in voluptate velit esse cillum dolore eu fugiat nulla pariatur. Excepteur sint occaecat cupidatat non proident, sunt in culpa qui officia deserunt mollit anim id est laborum.</p>
    <p class="body">Lorem ipsum dolor sit amet, consectetur adipisicing elit, sed do eiusmod tempor incididunt ut labore et dolore magna aliqua. Ut enim ad minim veniam, quis nostrud exercitation ullamco laboris nisi ut aliquip ex ea commodo consequat. Duis aute irure dolor in reprehenderit in voluptate velit esse cillum dolore eu fugiat nulla pariatur. Excepteur sint occaecat cupidatat non proident, sunt in culpa qui officia deserunt mollit anim id est laborum.</p>
    <p class="body">Lorem ipsum dolor sit amet, consectetur adipisicing elit, sed do eiusmod tempor incididunt ut labore et dolore magna aliqua. Ut enim ad minim veniam, quis nostrud exercitation ullamco laboris nisi ut aliquip ex ea commodo consequat. Duis aute irure dolor in reprehenderit in voluptate velit esse cillum dolore eu fugiat nulla pariatur. Excepteur sint occaecat cupidatat non proident, sunt in culpa qui officia deserunt mollit anim id est laborum.</p>
  </section>

  <section class="abs programs">
    <div class="tab">The Best Programs...</div>
    <p class="book">Book Now <b>▸</b></p>
    <div class="prog" style="border-top:0"><h3>Weight Loss Retreat</h3><em>Lasting weight loss results</em><p class="links">Program details | Typical Day<br>Dates &amp; Rates | FREE Brochure</p></div>
    <div class="prog"><h3>Residential Boot Camp</h3><em>Kick start your health &amp; fitness</em><p class="links">Program details | Typical Day<br>Dates &amp; Rates | FREE Brochure</p></div>
    <div class="prog"><h3>At Home Program</h3><em>Do it yourself with our home pack</em><p class="links">Program details | FREE Brochure</p></div>
    <div class="prog"><h3>Fitness Days</h3><em>Have fun and keep on track</em><p class="links">Program details | Typical Day<br>Dates &amp; Rates | FREE Brochure</p></div>
    <div class="prog"><h3>Local Group Exercise</h3><em>Get fit &amp; lose weight locally</em><p class="links">Overview | Times &amp; Locations</p></div>
    <div class="prog"><h3>Personal Training for you</h3><em>Find an approved FitWave Trainer</em></div>
  </section>

  <aside class="abs locations">
    <div class="grey-tab">The Best Location</div>
    <p class="loc-note">&amp; 1st Class Facilities</p>
    <div class="loc">
      <div class="shot" role="img" aria-label="Mountain lake scenery" style="background:linear-gradient(#6f97c4,#4d6f8c 45%,#3f5a3a)"></div>
      <div class="cap"><h4>Blue Mountains****</h4><p>4 star accommodation, stunning<br>mountain scenery &amp; 1st class facilities</p><p class="l"><span>Find out more</span><span>FREE Brochure</span><span>Book</span></p></div>
    </div>
    <div class="loc">
      <div class="shot" role="img" aria-label="Tropical beach with palm trees" style="background:linear-gradient(#3a8fc8,#4fb1c6 45%,#d9cfa8)"></div>
      <div class="cap"><h4>Sunshine Coast****</h4><p>4.5 star accommodation</p><p class="l"><span>Find out more</span><span>FREE Brochure</span><span>Book</span></p></div>
    </div>
    <div class="selector"><h5>Your Goal Selector</h5><p>Tell us your goal and we'll tell you how<br>FitWave can help</p><div class="sel-row"><span></span><b>Send</b></div></div>
    <blockquote class="testi">"The best weight loss experience in my life"</blockquote>
    <p class="testi-by">John Doe, Queensland</p>
  </aside>

  <section class="abs results">
    <div class="abs people" role="img" aria-label="Group of smiling women of different ages and sizes"></div>
    <div class="abs real">
      <h3>Real People - Real Results</h3>
      <ul><li>100's of people helped by FitWave</li><li>People of all ages, shapes, and sizes</li><li>Normal people just like you.</li></ul>
      <p class="rev">Testimonials &amp; Reviews <span style="color:var(--orange)">▸</span></p>
    </div>
    <div class="abs achieved">
      <h4>Results our clients have achieved</h4>
      <div class="ach-cols">
        <ul><li><svg class="tick"><use href="#tick"/></svg>Weight Loss</li><li><svg class="tick"><use href="#tick"/></svg>Fat loss</li><li><svg class="tick"><use href="#tick"/></svg>Eliminate high blood pressure</li><li><svg class="tick"><use href="#tick"/></svg>Eliminate type 2 Diabetes</li><li><svg class="tick"><use href="#tick"/></svg>Increased flexibility</li><li><svg class="tick"><use href="#tick"/></svg>Transform you skin condition</li><li><svg class="tick"><use href="#tick"/></svg>Feel happier</li><li><svg class="tick"><use href="#tick"/></svg>Better sleep patterns</li></ul>
        <ul><li><svg class="tick"><use href="#tick"/></svg>Weight Loss</li><li><svg class="tick"><use href="#tick"/></svg>Fat loss</li><li><svg class="tick"><use href="#tick"/></svg>Eliminate high blood pressure</li><li><svg class="tick"><use href="#tick"/></svg>Eliminate type 2 Diabetes</li><li><svg class="tick"><use href="#tick"/></svg>Increased flexibility</li><li><svg class="tick"><use href="#tick"/></svg>Transform you skin condition</li><li><svg class="tick"><use href="#tick"/></svg>Feel happier</li><li><svg class="tick"><use href="#tick"/></svg>Better sleep patterns</li></ul>
      </div>
    </div>
  </section>
</main>

<footer class="abs site-foot">
  <div class="abs foot-cols">
    <div class="foot-col"><h6>The Best Programs</h6>Weight Loss Retreat<br>Residential Boot Camp<br>Fitness Days<br>At Home Program<br>Local Group Exercise</div>
    <div class="foot-col"><h6>The Best Locations</h6>Blue Mountains, NSW<br>Sunshine Coast, QLD<br>Local Programs</div>
    <div class="foot-col"><h6>About Us</h6>Why Choose FitWave<br>Expert Team<br>What Clients Say<br>Contact Us<br>Book Now</div>
    <div class="foot-col"><h6>Results For...</h6>Fitness Goals<br>Diabetes Reduction<br>Blood Pressure Reduction<br>Depression Improvement<br>More Health Benefits</div>
    <div class="foot-col"><h6>FREE Information</h6>Request a Brochure<br>FREE FitWave Magazine</div>
  </div>
  <div class="abs foot-bar"><span>Copyright © 2011 FitWave Wellbeing PTY Ltd | ABN 12345678987</span><span>Contact Us | Book Now | Privacy</span></div>
</footer>

</body>
</html>
```